red quince
silk in motion
Modern
Dunmore Court
Harbor & Vale
Carmel, CA 93921
info@red-quince-shop.com
www.red-quince-shop.com
I'd like the card to be vertical, not horizontal! The logo should be centered!!!
should be the same, except the address:
P.O.Box 4819
Carmel, CA 93921-4819
logo should be centered on a vertical double sided business card!

```html
<!DOCTYPE html>
<html lang="en">
<head>
<meta charset="utf-8">
<title>red quince — stationery set</title>
<link href="https://fonts.googleapis.com/css2?family=Raleway:wght@300;400;600&display=swap" rel="stylesheet">
<style>
  :root {
    --navy: #1d3b7c;
    --sky: #2aa6df;
    --sky-pale: #cfe9f6;
    --paper: #ffffff;
    --stage: #e9e4dc;
    --ink: #4a5a70;
    --faint: rgba(42,166,223,0.14);
  }
  * { box-sizing: border-box; margin: 0; padding: 0; }
  html, body { width: 1200px; height: 422px; overflow: hidden; }
  body {
    position: relative;
    background: var(--stage);
    font-family: "Raleway", sans-serif;
    color: var(--ink);
  }
  .piece {
    position: absolute;
    background: var(--paper);
    box-shadow: 0 2px 6px rgba(0,0,0,0.25);
    overflow: hidden;
  }
  .label {
    position: absolute;
    font-size: 6px;
    color: #6b5a48;
    text-align: center;
  }
  .wave { position: absolute; left: 0; bottom: 0; width: 100%; }

  .brand { display: flex; flex-direction: column; align-items: center; }
  .brand-dot { border-radius: 50%; background: var(--sky); }
  .brand-name { font-weight: 400; color: var(--navy); white-space: nowrap; }

  /* business cards */
  .card-front { left: 24px; top: 115px; width: 53px; height: 173px; }
  .card-front .brand { margin-top: 22px; }
  .card-front .brand-dot { width: 16px; height: 16px; margin-bottom: 3px; }
  .card-front .brand-name { font-size: 8px; }
  .card-front .tagline { font-size: 3.5px; text-align: center; margin-top: 2px; color: var(--sky); }
  .card-front .contact { font-size: 3.2px; line-height: 1.45; text-align: center; margin-top: 14px; }
  .card-back { left: 91px; top: 115px; width: 53px; height: 173px; background: var(--navy); }
  .card-back .brand { margin-top: 58px; }
  .card-back .brand-dot { width: 18px; height: 18px; margin-bottom: 4px; background: var(--paper); }
  .card-back .brand-name { font-size: 8px; color: var(--paper); }

  /* letterheads */
  .letterhead { top: 29px; width: 293px; height: 384px; }
  .lh-one { left: 233px; }
  .lh-two { left: 559px; }
  .letterhead .mark { position: absolute; left: 126px; top: 12px; }
  .letterhead .mark .brand-dot { width: 24px; height: 24px; margin-bottom: 3px; }
  .letterhead .mark .brand-name { font-size: 9px; }
  .letterhead .address { position: absolute; right: 14px; top: 14px; font-size: 4px; line-height: 1.5; text-align: right; }
  .letterhead .side { position: absolute; right: 14px; top: 84px; font-size: 4px; line-height: 1.5; text-align: right; }
  .ghost { position: absolute; left: 50%; top: 118px; transform: translateX(-50%); }
  .ghost .brand-dot { width: 120px; height: 120px; background: var(--faint); }
  .ghost .brand-name { position: absolute; top: 44px; left: 50%; transform: translateX(-50%); font-size: 30px; font-weight: 300; color: rgba(29,59,124,0.16); }

  /* envelopes */
  .envelope { left: 880px; width: 296px; }
  .env-back-navy { top: 36px; height: 80px; }
  .env-back-sky { top: 92px; height: 100px; }
  .env-back-plain { top: 196px; height: 82px; left: 886px; width: 290px; }
  .env-front { top: 250px; height: 158px; left: 886px; width: 290px; }
  .envelope svg.flap { position: absolute; inset: 0; width: 100%; height: 100%; }
  .flap-mark { position: absolute; left: 50%; transform: translateX(-50%); }
  .flap-mark .brand-dot { width: 14px; height: 14px; margin-bottom: 2px; }
  .flap-mark .brand-name { font-size: 5px; }
  .env-front .mark { position: absolute; left: 10px; top: 8px; }
  .env-front .mark .brand-dot { width: 18px; height: 18px; margin-bottom: 2px; }
  .env-front .mark .brand-name { font-size: 6px; }
  .env-front .ret { position: absolute; left: 10px; top: 40px; font-size: 3.6px; line-height: 1.45; }
  .env-front .ghost { left: 200px; top: 40px; }
  .env-front .ghost .brand-dot { width: 70px; height: 70px; }
  .env-front .ghost .brand-name { font-size: 14px; top: 26px; }
</style>
</head>
<body>

  <!-- business card front -->
  <section class="piece card-front">
    <div class="brand">
      <div class="brand-dot"></div>
      <div class="brand-name">red quince</div>
    </div>
    <p class="tagline">silk in motion</p>
    <p class="contact">Dunmore Court<br>Harbor &amp; Vale<br>P.O.Box 4819<br>Carmel, CA 93921-4819<br>info@red-quince-shop.com<br>www.red-quince-shop.com</p>
    <svg class="wave" viewBox="0 0 53 24" height="24" preserveAspectRatio="none">
      <path d="M0 10 Q26 24 53 6 L53 24 L0 24Z" fill="var(--sky)"/>
      <path d="M0 16 Q26 26 53 12 L53 24 L0 24Z" fill="var(--navy)"/>
    </svg>
  </section>
  <p class="label" style="left:24px;top:292px;width:53px">Front card</p>

  <!-- business card back -->
  <section class="piece card-back">
    <div class="brand">
      <div class="brand-dot"></div>
      <div class="brand-name">red quince</div>
    </div>
  </section>
  <p class="label" style="left:91px;top:292px;width:53px">Back card</p>

  <!-- letterhead page 1 -->
  <section class="piece letterhead lh-one">
    <div class="brand mark"><div class="brand-dot"></div><div class="brand-name">red quince</div></div>
    <p class="address">info@red-quince-shop.com<br>www.red-quince-shop.com</p>
    <p class="side">Dunmore Court<br>Harbor &amp; Vale<br>P.O.Box 4819<br>Carmel, CA<br>93921-4819</p>
    <div class="brand ghost"><div class="brand-dot"></div><div class="brand-name">red quince</div></div>
    <svg class="wave" viewBox="0 0 293 40" height="40" preserveAspectRatio="none">
      <path d="M0 22 Q140 44 293 12 L293 40 L0 40Z" fill="var(--sky)"/>
      <path d="M0 30 Q150 46 293 22 L293 40 L0 40Z" fill="var(--navy)"/>
    </svg>
  </section>
  <p class="label" style="left:233px;top:415px;width:293px">Letterhead page 1</p>

  <!-- letterhead page 2 -->
  <section class="piece letterhead lh-two">
    <div class="brand ghost"><div class="brand-dot"></div><div class="brand-name">red quince</div></div>
    <svg class="wave" viewBox="0 0 293 40" height="40" preserveAspectRatio="none">
      <path d="M0 22 Q140 44 293 12 L293 40 L0 40Z" fill="var(--sky)"/>
      <path d="M0 30 Q150 46 293 22 L293 40 L0 40Z" fill="var(--navy)"/>
    </svg>
  </section>
  <p class="label" style="left:559px;top:415px;width:293px">Letterhead page 2</p>

  <!-- envelope back, navy flap -->
  <section class="piece envelope env-back-navy">
    <svg class="flap" viewBox="0 0 296 80" preserveAspectRatio="none">
      <rect width="296" height="80" fill="var(--paper)"/>
      <path d="M0 0 L296 0 L296 30 Q148 62 0 30Z" fill="var(--navy)"/>
    </svg>
    <div class="brand flap-mark" style="top:20px">
      <div class="brand-dot" style="background:var(--paper)"></div>
      <div class="brand-name" style="color:var(--paper)">red quince</div>
    </div>
  </section>

  <!-- envelope back, sky flap -->
  <section class="piece envelope env-back-sky">
    <svg class="flap" viewBox="0 0 296 100" preserveAspectRatio="none">
      <rect width="296" height="100" fill="var(--paper)"/>
      <path d="M0 0 L296 0 L296 40 Q148 74 0 40Z" fill="var(--sky)"/>
    </svg>
    <div class="brand flap-mark" style="top:30px">
      <div class="brand-dot" style="background:var(--navy)"></div>
      <div class="brand-name">red quince</div>
    </div>
  </section>

  <!-- envelope back, plain -->
  <section class="piece envelope env-back-plain">
    <svg class="flap" viewBox="0 0 290 82" preserveAspectRatio="none">
      <path d="M0 0 L145 42 L290 0" fill="none" stroke="#d6dde4" stroke-width="1"/>
      <path d="M0 82 L120 36 M290 82 L170 36" fill="none" stroke="#e3e8ed" stroke-width="1"/>
    </svg>
  </section>

  <!-- envelope front -->
  <section class="piece envelope env-front">
    <div class="brand mark"><div class="brand-dot"></div><div class="brand-name">red quince</div></div>
    <p class="ret">Dunmore Court<br>Harbor &amp; Vale<br>P.O.Box 4819<br>Carmel, CA 93921-4819</p>
    <div class="brand ghost"><div class="brand-dot"></div><div class="brand-name">red quince</div></div>
    <svg class="wave" viewBox="0 0 290 24" height="24" preserveAspectRatio="none">
      <path d="M0 12 Q140 28 290 6 L290 24 L0 24Z" fill="var(--sky)"/>
      <path d="M0 18 Q150 28 290 13 L290 24 L0 24Z" fill="var(--navy)"/>
    </svg>
  </section>
  <p class="label" style="left:886px;top:410px;width:290px">Envelopes DL</p>

</body>
</html>
```